Consulting im Pharmaproduktionsbereich sucht Webdesign
Zielgruppe
Consulting im Pharmaproduktionsbereich.
Bitte lesen Sie dazu die PowerPoint.
Aufgabenstellung
Im Anhang finden Sie eine Powerpoint Datei, von welcher die 'Home' und 'Referenz'seite Teil dieser Auschreibung sind.

```html
<!DOCTYPE html>
<html lang="de">
<head>
<meta charset="utf-8">
<title>verano tec – Pharma-Produktion</title>
<link rel="stylesheet" href="https://fonts.googleapis.com/css2?family=Raleway:wght@300;400;500;600;700&display=swap">
<style>
:root{
  --navy:#1a2a40;
  --navy-deep:#1b2b43;
  --aqua:#6cc0d5;
  --paper:#f5f9fc;
  --white:#ffffff;
  --ink:#1c2b3f;
  --body:#3a4a5e;
}
*{margin:0;padding:0;box-sizing:border-box}
html,body{width:1200px;height:2173px;overflow:hidden}
body{position:relative;font-family:"Raleway",sans-serif;background:var(--white);color:var(--ink)}
a{color:inherit;text-decoration:none}

/* hero */
.hero{position:absolute;left:0;top:0;width:1200px;height:607px;overflow:hidden}
.hero-photo{position:absolute;inset:0;background:linear-gradient(90deg,#0e0f12 0%,#3d3e42 22%,#6f7276 45%,#8a8d90 70%,#9a9c9e 100%)}
.hero-accent{position:absolute;right:0;top:158px;width:250px;height:449px;background:linear-gradient(90deg,rgba(95,182,207,0) 0%,rgba(95,182,207,.45) 55%,rgba(95,182,207,.7) 100%)}
.brand{position:absolute;left:112px;top:44px;display:flex;align-items:center;gap:6px;color:var(--white);font-weight:500;font-size:20px;letter-spacing:.2px}
.brand-mark{width:14px;height:14px;border:2px solid currentColor;border-radius:2px}
.nav a{position:absolute;top:48px;color:var(--white);font-size:13px;letter-spacing:.4px;white-space:nowrap}
.headline{position:absolute;left:112px;color:var(--white);font-weight:700;font-size:31px;line-height:40px;letter-spacing:-.4px}
.tagline{position:absolute;left:112px;top:469px;color:var(--aqua);font-size:17px;font-weight:400}
.btn{position:absolute;left:407px;top:463px;width:115px;height:40px;background:var(--aqua);color:var(--white);font-weight:700;font-size:12.5px;letter-spacing:.3px;display:flex;align-items:center;justify-content:center;border-radius:2px}

/* how we work */
.work{position:absolute;left:0;top:607px;width:1200px;height:1073px;background:var(--paper)}
.work-title{position:absolute;left:112px;top:82px;color:var(--aqua);font-weight:700;font-size:31px}
.step-art{position:absolute;left:195px;width:205px;border-radius:10px;background:linear-gradient(160deg,#e6eef5,#dbe5ee)}
.step{position:absolute;left:530px;width:557px}
.step h3{font-size:30px;font-weight:600;color:var(--ink);letter-spacing:-.2px}
.step p{margin-top:26px;font-size:14.2px;font-weight:300;line-height:23px;letter-spacing:.15px;color:var(--body)}
.step-rule{position:absolute;left:530px;width:557px;height:3px;background:var(--aqua)}

/* footer */
.footer{position:absolute;left:0;top:1723px;width:1200px;height:450px;background:var(--navy);overflow:hidden}
.footer-accent{position:absolute;left:0;top:0;width:130px;height:339px;background:linear-gradient(90deg,rgba(95,182,207,.75) 0%,rgba(95,182,207,.45) 60%,rgba(95,182,207,0) 100%)}
.footer .brand{top:72px;left:113px}
.f-col{position:absolute;top:76px}
.f-col h4{color:var(--aqua);font-size:18px;font-weight:600;letter-spacing:.2px}
.f-col ul{list-style:none;margin-top:20px}
.f-col li{color:var(--white);font-size:13px;line-height:21px;margin-bottom:7.5px}
.f-bottom{position:absolute;left:0;top:339px;width:1200px;height:111px;background:var(--navy-deep);border-top:1px solid #2c3d56}
.copyright{position:absolute;left:54px;top:33px;color:var(--white);font-size:10.5px;font-weight:500}
.lang{position:absolute;left:54px;top:58px;color:var(--white);font-size:10px;letter-spacing:2px;font-weight:500;display:flex;align-items:center;gap:10px}
</style>
</head>
<body>

<header class="hero">
  <div class="hero-photo" role="img" aria-label="Photo of a lab technician in a hairnet looking into a microscope"></div>
  <div class="hero-accent" role="img" aria-label="Decorative aqua wave shape at the right edge"></div>
  <a class="brand" href="#"><span class="brand-mark"></span>verano tec</a>
  <nav class="nav">
    <a href="#" style="left:696px">HOME</a>
    <a href="#" style="left:783px">REFERENZEN</a>
    <a href="#" style="left:909px">KONTAKT</a>
    <a href="#" style="left:1010px">IMPRESSUM</a>
  </nav>
  <h1 class="headline" style="top:177px">Als spezialisierter Anbieter schaffen wir Wert in der<br>Pharma-Produktion</h1>
  <h2 class="headline" style="top:296px">Mit langjähriger Erfahrung in Abläufen und<br>überlegener Technologie setzt ein Netzwerk von<br>Spitzenleuten schnell und pragmatisch um</h2>
  <p class="tagline">Sicht- und messbar in Ihrer Bilanz</p>
  <a class="btn" href="#">KONTAKT</a>
</header>

<main class="work">
  <h2 class="work-title">How We Work</h2>

  <div class="step-art" style="top:191px;height:202px" role="img" aria-label="Line illustration of a robotic arm"></div>
  <article class="step" style="top:218px">
    <h3>Abläufe</h3>
    <p>Wir hinterfragen gewachsene Strukturen und reduzieren deren Komplexität, indem durch Modellierung neue Standards gefunden werden. Das ist die Voraussetzung Ihre Kosten weiter zu senken.</p>
  </article>
  <div class="step-rule" style="top:390px"></div>

  <div class="step-art" style="top:465px;height:202px" role="img" aria-label="Line illustration of a chip with a brain symbol"></div>
  <article class="step" style="top:483px">
    <h3>Technologie</h3>
    <p>Wir bringen langjährige Expertise sowohl im klassischen Maschinenbau als auch in moderner IT mit. Künstliche Intelligenz, Augmented Reality, Algorithmik und Robotiks – wir bedienen uns eines breiten Portfolios und wir wissen, welche Prozesse mit welchen Maschinen in einer Produktionsumgebung robust laufen.</p>
  </article>
  <div class="step-rule" style="top:665px"></div>

  <div class="step-art" style="top:740px;height:203px" role="img" aria-label="Line illustration of a cube on a stand"></div>
  <article class="step" style="top:757px">
    <h3>Wert</h3>
    <p>Ob Sie Topline mehr Kapazität generieren wollen, oder Bottomline einzelne Kostenpositionen reduzieren: Wir achten auf das für Ihren Betrieb passende Werteversprechen und liefern schnell ergebniswirksam. Unnötiger Firlefanz bleibt weg.</p>
  </article>
  <div class="step-rule" style="top:939px"></div>
</main>

<footer class="footer">
  <div class="footer-accent" role="img" aria-label="Decorative aqua wave shape at the left edge"></div>
  <a class="brand" href="#"><span class="brand-mark"></span>verano tec</a>

  <div class="f-col" style="left:372px">
    <h4>COMPANY</h4>
    <ul><li>Terms &amp; Condition</li><li>Privacy Policy</li><li>Refund Policy</li><li>Legal Disclaimer</li><li>Affiliate Program</li></ul>
  </div>
  <div class="f-col" style="left:603px">
    <h4>REFERENZEN</h4>
    <ul><li>Time Tracking</li><li>Geographische<br>Lokalisierung</li><li>Org Chart</li><li>OEE</li><li>More</li></ul>
  </div>
  <div class="f-col" style="left:780px">
    <h4>RESOURCES</h4>
    <ul><li>Support</li><li>Contact Us</li></ul>
  </div>
  <div class="f-col" style="left:980px">
    <h4>CONNECT</h4>
    <ul><li>Friendspace</li><li>Chirper</li><li>Vidstream</li><li>Pictogram</li></ul>
  </div>

  <div class="f-bottom">
    <p class="copyright">Copyright © 2019 Veranotec, LLC All Rights Reserved</p>
    <p class="lang">ENGLISH
      <svg width="8" height="5" viewBox="0 0 8 5" aria-hidden="true"><path d="M1 1 L4 4 L7 1" fill="none" stroke="#ffffff" stroke-width="1"/></svg>
    </p>
  </div>
</footer>

</body>
</html>
```